Professional and creatice Life Coach - Business Card design

I just relaunched my website and now i a need a correspoonding business card for my task as life coach. My website is www.dlorvan.net as reference. The compass is kind of a symbol for my work, as I help people navigate through their challenging phases in life. The business card should be colorful, but not too playful as I also adress business people. So it sould be creative, but professional (also to suport my other business as Management Consultant)

Target Market(s)

People who want to get teir problems resolved, in business, partnership and other personal realms

Industry/Entity Type

Life Coaching

Contact Information for Business Card

Front side should include Name, Phone number, Email, Website and address

Font styles to use
Sans Serif

Colors
add136

Requirements
Must have
• "Mag. Benedikt Haufmoll" -> Name
"Energetische Praxis" -> Jobtitle (describing my profession as life coach)
colours and style should match my website www.dlorvan.net
Nice to have
• a compass as a symbol

```html
<!DOCTYPE html>
<html lang="de">
<head>
<meta charset="utf-8">
<title>Benedikt Haufmoll – Visitenkarte</title>
<link rel="stylesheet" href="https://fonts.googleapis.com/css2?family=Playfair+Display:wght@400&family=Montserrat:wght@500;600&display=swap">
<style>
  :root{
    --stage:#2b2e33;
    --card:#ffffff;
    --forest:#2f3b2d;
    --lime:#a7c155;
    --ink:#1d1f1c;
    --mark:#5d6659;
  }
  *{box-sizing:border-box;margin:0;padding:0}
  html,body{width:1200px;height:900px;overflow:hidden}
  body{background:var(--stage);display:flex;flex-direction:column;align-items:center;justify-content:center;gap:60px}
  .card{position:relative;width:600px;height:343px;background:var(--card);border-radius:22px;overflow:hidden;box-shadow:0 14px 30px rgba(0,0,0,.35)}
  .card-shapes{position:absolute;inset:0;width:100%;height:100%}
  .shape-forest{fill:var(--forest)}
  .shape-lime{fill:var(--lime)}
  .wordmark{position:absolute;display:flex;align-items:center;gap:12px;font-family:"Playfair Display",Georgia,serif;font-weight:400;color:var(--ink)}
  .wordmark-dot{border-radius:50%;border:2px solid var(--mark);flex:none}
  .card-front .wordmark{left:170px;top:105px;font-size:40px}
  .card-front .wordmark-dot{width:46px;height:46px}
  .card-back .wordmark{left:38px;top:34px;font-size:22px}
  .card-back .wordmark-dot{width:28px;height:28px}
  .contact-list{position:absolute;left:40px;top:88px;list-style:none;font-family:"Montserrat",Arial,sans-serif;font-weight:600;font-size:15px;color:var(--ink)}
  .contact-list li{display:flex;align-items:center;gap:14px;height:32px}
  .contact-icon{width:16px;height:16px;fill:none;stroke:var(--ink);stroke-width:1.5}
  .holder{position:absolute;right:40px;top:150px;text-align:left}
  .holder-name{font-family:"Playfair Display",Georgia,serif;font-size:26px;color:var(--ink);padding-left:34px}
  .holder-rule{display:block;width:70px;height:1.5px;background:var(--ink);margin:2px 0 3px}
  .holder-title{font-family:"Montserrat",Arial,sans-serif;font-weight:600;font-size:15px;color:var(--ink);padding-left:70px;margin-top:-2px}
  .faint-disc{position:absolute;left:415px;top:258px;width:62px;height:62px;border-radius:50%;border:2px solid rgba(255,255,255,.12)}
</style>
</head>
<body>

<section class="card card-front" aria-label="Vorderseite">
  <svg class="card-shapes" viewBox="0 0 600 343" preserveAspectRatio="none" aria-hidden="true">
    <path class="shape-forest" d="M0,0 H130 C80,50 40,120 0,190 Z"/>
    <path class="shape-lime" d="M95,0 H120 C100,70 120,140 190,190 C120,160 80,90 95,0 Z"/>
    <path class="shape-forest" d="M0,343 V300 C220,330 380,170 600,160 V343 Z"/>
  </svg>
  <div class="wordmark"><span class="wordmark-dot"></span>Benedikt Haufmoll</div>
</section>

<section class="card card-back" aria-label="Rückseite mit Kontaktdaten">
  <svg class="card-shapes" viewBox="0 0 600 343" preserveAspectRatio="none" aria-hidden="true">
    <path class="shape-forest" d="M430,0 H600 V130 C570,70 510,25 430,0 Z"/>
    <path class="shape-lime" d="M250,262 C400,268 520,296 600,318 V330 C510,300 400,272 250,262 Z"/>
    <path class="shape-forest" d="M0,200 C120,300 380,270 600,333 V343 H0 Z"/>
  </svg>
  <div class="wordmark"><span class="wordmark-dot"></span>Benedikt Haufmoll</div>
  <ul class="contact-list">
    <li><svg class="contact-icon" viewBox="0 0 16 16"><path d="M4 1.5 L6.5 4.5 L5 6.5 C6 8.5 7.5 10 9.5 11 L11.5 9.5 L14.5 12 L12.5 14.5 C7 14 2 9 1.5 3.5 Z"/></svg>098 765 43210</li>
    <li><svg class="contact-icon" viewBox="0 0 16 16"><rect x="1.5" y="3.5" width="13" height="9"/><path d="M1.5 3.5 L8 9 L14.5 3.5"/></svg>b.haufmoll@mailbox.net</li>
    <li><svg class="contact-icon" viewBox="0 0 16 16"><circle cx="8" cy="8" r="6.5"/><ellipse cx="8" cy="8" rx="2.8" ry="6.5"/><path d="M1.5 8 H14.5"/></svg>www.dlorvan.net</li>
  </ul>
  <div class="holder">
    <p class="holder-name">Mag. Benedikt Haufmoll</p>
    <span class="holder-rule"></span>
    <p class="holder-title">Energetische Praxis</p>
  </div>
  <span class="faint-disc" aria-hidden="true"></span>
</section>

</body>
</html>
```